Business Card Design For A Renovation Contractor Company

We need a business card for a new company based in Singapore, our company name is "KT Planora". We are a renovation contractor that builds designs into reality. We build more of F&B restaurants, retail stores and commercial offices. We work very closely with designers. The final design should communicate to our client that we are a company that you can trust, that will plan and complete your project without giving you a headache. I like my client to remember my company as "KT". The beauty of SIMPLE is important.

Industry/Entity Type

Contractor

Requirements
Nice to have
• Black or Red base

```html
<!DOCTYPE html>
<html lang="en">
<head>
<meta charset="utf-8">
<title>KT Planora – Business Card</title>
<link href="https://fonts.googleapis.com/css2?family=Questrial&display=swap" rel="stylesheet">
<style>
  :root {
    --paper: #ffffff;
    --ink: #1a1a1a;
    --brand-red: #d92128;
    --card-border: #d4d4d4;
    --on-red: #ffffff;
  }
  * { margin: 0; padding: 0; box-sizing: border-box; }
  html, body { width: 1200px; height: 1000px; overflow: hidden; background: var(--paper); }
  body { position: relative; font-family: "Questrial", sans-serif; color: var(--ink); }

  .card { position: absolute; left: 314px; width: 572px; height: 350px; }
  .card--front { top: 119px; background: var(--paper); border: 1px solid var(--card-border); }
  .card--back { top: 531px; background: var(--brand-red); overflow: hidden; }

  .brand-dot {
    position: absolute; left: 227px; top: 52px; width: 110px; height: 110px;
    border-radius: 50%; background: var(--brand-red);
  }
  .wordmark {
    position: absolute; left: 0; right: 0; top: 168px; text-align: center;
    font-size: 54px; line-height: 1; letter-spacing: 1px; color: var(--ink); font-weight: 400;
    white-space: nowrap;
  }
  .wordmark-rule {
    position: absolute; left: 127px; width: 318px; top: 221px; height: 3px; background: var(--ink);
  }
  .tagline {
    position: absolute; left: 0; right: 0; top: 225px; text-align: center;
    font-size: 19px; line-height: 1.1; letter-spacing: 0.6px; color: var(--ink); white-space: nowrap;
  }

  .holder { position: absolute; left: 220px; top: 106px; }
  .holder-name { font-size: 22px; color: var(--ink); letter-spacing: 0.4px; -webkit-text-stroke: 0.6px var(--ink); }
  .holder-role { font-size: 18px; font-style: italic; color: var(--ink); margin-top: 2px; }

  .contact { position: absolute; left: 184px; top: 173px; color: var(--on-red); font-size: 19px; line-height: 24.7px; letter-spacing: 0.8px; white-space: nowrap; }
  .contact-row { display: flex; }
  .contact-label { width: 20px; text-align: right; -webkit-text-stroke: 0.6px var(--on-red); }
  .contact-sep { width: 12px; text-align: center; }
  .contact-value { padding-left: 4px; }
  .contact-value--indent { padding-left: 36px; }
</style>
</head>
<body>
  <section class="card card--front" aria-label="Card front">
    <div class="brand-dot" aria-hidden="true"></div>
    <div class="wordmark">KT Planora</div>
    <div class="wordmark-rule" aria-hidden="true"></div>
    <div class="tagline">turning plans into real spaces</div>
  </section>

  <section class="card card--back" aria-label="Card back">
    <div class="holder">
      <div class="holder-name">Kelvin Tan</div>
      <div class="holder-role">Director</div>
    </div>
    <div class="contact">
      <div class="contact-row"><span class="contact-label">A</span><span class="contact-sep">-</span><span class="contact-value">8 Keppel Lane</span></div>
      <div class="contact-row"><span class="contact-value contact-value--indent">#03-210 Keppel Hub</span></div>
      <div class="contact-row"><span class="contact-value contact-value--indent">Singapore 098765</span></div>
      <div class="contact-row"><span class="contact-label">M</span><span class="contact-sep">-</span><span class="contact-value">6591234470</span></div>
      <div class="contact-row"><span class="contact-label">E</span><span class="contact-sep">-</span><span class="contact-value">kelvin@ktplanora.com</span></div>
    </div>
  </section>
</body>
</html>
```